Design for a 4 screens mobile app: Brelluvo

The app is a compact but illustrated phone/address book...
We need a design for the 5 screens of the app (see screens attached):
a) "index" : 1 screen with 6 pictures of contact person
b) "contact list" : 1 screen, to manage (add/del/edit) the contacts of the phone/address book
c) "add contact" : 1 screen to add a contact (a picture + a phone number)
d) "update contact" : similar to "add"
e) "fields missing" : add/edit screens in "error" state
We also need the ico design + loading screen.
No specific guidelines, nor logo or whatever.
It will be a free app distributed on iOS and Androïd.
We just want to make it looking nice & very usable for end users.
B2C

```html
<!DOCTYPE html>
<html lang="en">
<head>
<meta charset="utf-8">
<title>Brelluvo – Add Contact Screen</title>
<link href="https://fonts.googleapis.com/css2?family=Lato:wght@300;400;700&display=swap" rel="stylesheet">
<style>
  :root{
    --coral:#f37574;
    --coral-soft:#f6a09f;
    --screen-bg:#f0f0f0;
    --icon-grey:#999999;
    --icon-light:#c4c4c4;
    --green:#4cb848;
    --white:#ffffff;
  }
  html,body{margin:0;padding:0;overflow:hidden;}
  body{width:1200px;height:675px;background:var(--coral);font-family:'Lato',sans-serif;}
  .canvas{position:relative;width:1366px;height:768px;transform:scale(0.8785);transform-origin:0 0;background:var(--coral);overflow:hidden;}
  .app-screen{position:absolute;left:151px;top:199px;width:318px;height:569px;background:var(--screen-bg);overflow:hidden;}
  .status-bar{height:18px;background:var(--coral);color:var(--white);font-size:9px;font-weight:700;display:flex;align-items:center;justify-content:space-between;padding:0 7px;box-sizing:border-box;}
  .status-left,.status-right{display:flex;align-items:center;gap:4px;width:90px;}
  .status-right{justify-content:flex-end;}
  .status-time{font-size:9.5px;}
  .nav-bar{height:40px;background:var(--coral);color:var(--white);display:flex;align-items:center;justify-content:space-between;padding:0 13px;box-sizing:border-box;}
  .nav-title{font-weight:300;font-size:13px;}
  .photo-picker{position:absolute;left:85px;top:144px;width:148px;height:148px;border-radius:50%;background:var(--icon-grey);display:flex;align-items:center;justify-content:center;}
  .mobile-field{position:absolute;left:76px;top:418px;width:164px;height:38px;background:var(--coral);border-radius:2px;color:var(--coral-soft);font-size:15px;display:flex;align-items:center;justify-content:center;}
  .action-delete{position:absolute;left:77px;top:478px;}
  .action-gallery{position:absolute;left:201px;top:480px;}
  .screen-label{position:absolute;left:553px;top:404px;margin:0;color:var(--white);font-weight:300;font-size:38px;letter-spacing:0.3px;}
</style>
</head>
<body>
<div class="canvas">
  <section class="app-screen" aria-label="Add contact">
    <div class="status-bar">
      <div class="status-left">
        <svg width="14" height="6" viewBox="0 0 14 6"><g fill="#fff"><rect x="0" y="3" width="2" height="3"/><rect x="3" y="2" width="2" height="4"/><rect x="6" y="1" width="2" height="5"/><rect x="9" y="0" width="2" height="6"/><rect x="12" y="0" width="2" height="6"/></g></svg>
        <span>NB CZ</span>
        <svg width="11" height="8" viewBox="0 0 11 8"><path d="M0.5 2.6a7 7 0 0 1 10 0M2.3 4.3a4.5 4.5 0 0 1 6.4 0" stroke="#fff" stroke-width="1.3" fill="none"/><circle cx="5.5" cy="6.6" r="1.2" fill="#fff"/></svg>
      </div>
      <span class="status-time">2:52 PM</span>
      <div class="status-right">
        <svg width="10" height="10" viewBox="0 0 10 10"><circle cx="5" cy="5" r="4.2" stroke="#fff" stroke-width="1.2" fill="none"/><rect x="3.3" y="4.3" width="3.4" height="2.6" fill="#fff"/><path d="M3.9 4.4V3.5a1.1 1.1 0 0 1 2.2 0v.9" stroke="#fff" stroke-width="0.8" fill="none"/></svg>
        <span>53 %</span>
        <svg width="15" height="7" viewBox="0 0 15 7"><rect x="0.5" y="0.5" width="12" height="6" stroke="#fff" fill="none"/><rect x="1.5" y="1.5" width="6" height="4" fill="#fff"/><rect x="13.2" y="2.2" width="1.3" height="2.6" fill="#fff"/></svg>
      </div>
    </div>
    <header class="nav-bar">
      <svg class="nav-back" width="14" height="14" viewBox="0 0 14 14" aria-label="Back"><path d="M5 1 1 5l4 4V6.3c3.5 0 5.7 1.7 6 6.5 1.4-5-.6-8.8-6-9V1z" fill="#fff"/></svg>
      <span class="nav-title">Add Contact</span>
      <svg class="nav-save" width="15" height="15" viewBox="0 0 15 15" aria-label="Save"><circle cx="7.5" cy="7.5" r="7" fill="#fff"/><path d="M4.2 7.7l2.2 2.2 4.3-4.5" stroke="var(--coral)" stroke-width="1.8" fill="none"/></svg>
    </header>

    <div class="photo-picker" aria-label="Add photo">
      <svg width="92" height="64" viewBox="0 0 92 64">
        <path d="M8 10h16l6-8h24l6 8h20a4 4 0 0 1 4 4v44a4 4 0 0 1-4 4H8a4 4 0 0 1-4-4V14a4 4 0 0 1 4-4z" fill="#fff"/>
        <circle cx="47" cy="34" r="22" fill="var(--icon-grey)"/>
        <circle cx="49" cy="33" r="19" fill="#fff"/>
        <circle cx="49" cy="33" r="14" fill="var(--icon-grey)"/>
        <circle cx="49" cy="33" r="10.5" fill="#fff"/>
      </svg>
    </div>

    <div class="mobile-field">Mobile Number</div>

    <svg class="action-delete" width="38" height="40" viewBox="0 0 38 40" aria-label="Delete">
      <g fill="var(--icon-light)">
        <rect x="4" y="12" width="24" height="3" rx="1"/>
        <path d="M6 16h20l-2 22H8z"/>
        <path d="M4 8c5-7 16-8 23-2l3-3v9h-9l3-3c-5-4-12-4-17 1z"/>
        <path d="M29 18l7-8 2 2-7 8zM31 10l5 6-2 1-5-6z"/>
      </g>
      <g fill="var(--screen-bg)"><rect x="11" y="20" width="2" height="14"/><rect x="15.5" y="20" width="2" height="14"/><rect x="20" y="20" width="2" height="14"/></g>
    </svg>

    <svg class="action-gallery" width="40" height="38" viewBox="0 0 40 38" aria-label="Choose from contacts">
      <g fill="var(--green)">
        <rect x="9" y="11" width="28" height="24" rx="1.5" transform="rotate(10 23 23)"/>
        <rect x="5" y="6" width="28" height="24" rx="1.5" transform="rotate(5 19 18)"/>
        <rect x="1" y="1" width="28" height="24" rx="1.5"/>
      </g>
      <rect x="5" y="5" width="20" height="16" fill="#fff"/>
      <circle cx="15" cy="11" r="3.2" fill="var(--green)"/>
      <path d="M8.5 21c0-4.5 3-6.5 6.5-6.5s6.5 2 6.5 6.5z" fill="var(--green)"/>
    </svg>
  </section>

  <h1 class="screen-label">Add Contact Screen</h1>
</div>
</body>
</html>
```